Chinese New Year Party

To create an invitation for a party.

Invitation to be sent by email.
Party date : Feb 1 2014
RSVP : 22 Jan 2014 to lin@tealmeadow.net or otto@tealmeadow.net
address 17 Marlow Crescent, Singapore 568213
(add google map address)

Message : "We'd love you to join us as we celebrate Chinese New Year 2014 with some great music, some horses doeuvres, exotic cocktails, and top company.
We'll horse around a little as well ;)
Otto & Lin"

Theme of the invite should be Chinese/Oriental
Images should include a horse ( for the Chinese new year ) with the number 69 on the horse. Other images should include a DJ with music decks and images of cocktails.

Target Market(s)

Target market 30-40 year olds who enjoy nite clubs

```html
<!DOCTYPE html>
<html lang="en">
<head>
<meta charset="utf-8">
<title>Year of the Horse – Chinese New Year 2014 Celebration</title>
<link rel="stylesheet" href="https://fonts.googleapis.com/css2?family=Great+Vibes&family=Cinzel:wght@400&family=Source+Sans+3:wght@400&display=swap">
<style>
  :root {
    --page: #ffffff;
    --card-red: #bf1e2e;
    --card-red-deep: #a3141f;
    --shadow-red: #9c1822;
    --gold: #f2b51e;
    --gold-soft: #f6c54a;
    --ink-light: #ffffff;
    --map-grey: #e4e2dc;
  }
  html, body {
    margin: 0;
    width: 1200px;
    height: 900px;
    overflow: hidden;
    background: var(--page);
  }
  .invitation {
    position: absolute;
    left: 44px;
    top: 44px;
    width: 1112px;
    height: 820px;
    background: var(--card-red);
    overflow: hidden;
  }
  .invitation__frame {
    position: absolute;
    inset: 12px;
    border: 2px solid var(--gold);
    pointer-events: none;
  }
  .corner-ornament {
    position: absolute;
    width: 56px;
    height: 56px;
    background: var(--gold);
    border-radius: 10px;
  }
  .corner-ornament--tl { left: 4px; top: 4px; }
  .corner-ornament--tr { right: 4px; top: 4px; }
  .corner-ornament--bl { left: 4px; bottom: 4px; }
  .corner-ornament--br { right: 4px; bottom: 4px; }

  .crowd-silhouette {
    position: absolute;
    left: 150px;
    bottom: 0;
    width: 820px;
    height: 360px;
    background: linear-gradient(to top, var(--shadow-red) 0%, rgba(156,24,34,0.75) 45%, rgba(191,30,46,0) 100%);
  }
  .cocktail-glasses {
    position: absolute;
    left: 890px;
    top: 600px;
    width: 190px;
    height: 200px;
    background: linear-gradient(to top, var(--card-red-deep), rgba(163,20,31,0.35));
    border-radius: 12px 12px 0 0;
  }
  .horse-illustration {
    position: absolute;
    left: 700px;
    top: 36px;
    width: 400px;
    height: 600px;
    background: radial-gradient(ellipse at 45% 35%, rgba(242,181,30,0.55) 0%, rgba(242,181,30,0.25) 45%, rgba(191,30,46,0) 75%);
  }

  .headline {
    position: absolute;
    left: 92px;
    top: 96px;
    margin: 0;
    font-weight: 400;
    color: var(--ink-light);
  }
  .headline__lead {
    font-family: "Source Sans 3", sans-serif;
    font-size: 28px;
    vertical-align: 14px;
  }
  .headline__title {
    display: inline-block;
    font-family: "Great Vibes", cursive;
    color: var(--gold);
    font-size: 84px;
    line-height: 1;
  }
  .headline__title small {
    font-size: 44px;
  }
  .subtitle {
    position: absolute;
    left: 92px;
    top: 222px;
    margin: 0;
    font-family: "Cinzel", serif;
    font-weight: 400;
    font-size: 28px;
    letter-spacing: 0.5px;
    color: var(--gold);
  }
  .message {
    position: absolute;
    left: 92px;
    top: 288px;
    width: 620px;
    font-family: "Source Sans 3", sans-serif;
    font-size: 26px;
    line-height: 38px;
    color: var(--ink-light);
  }
  .message p { margin: 0 0 8px; }
  .hosts {
    position: absolute;
    left: 320px;
    top: 530px;
    margin: 0;
    font-family: "Great Vibes", cursive;
    font-size: 50px;
    color: var(--gold);
  }
  .location-map {
    position: absolute;
    left: 82px;
    top: 560px;
    width: 196px;
    height: 196px;
    border: 4px solid var(--gold-soft);
    background: var(--map-grey);
  }
  .details {
    position: absolute;
    left: 310px;
    top: 620px;
    margin: 0;
    font-family: "Source Sans 3", sans-serif;
    font-size: 26px;
    line-height: 34px;
    color: var(--ink-light);
  }
  .details dt {
    display: inline;
    font-family: "Cinzel", serif;
    color: var(--gold);
    font-size: 24px;
  }
  .details dd { display: inline; margin: 0; }
  .details__row { margin: 0; }
  .details__indent { padding-left: 54px; }
</style>
</head>
<body>
  <main class="invitation">
    <div class="crowd-silhouette" role="img" aria-label="Silhouettes of party guests dancing with raised arms and a DJ at the decks"></div>
    <div class="cocktail-glasses" role="img" aria-label="Silhouettes of cocktail glasses with citrus slices"></div>
    <div class="horse-illustration" role="img" aria-label="Stylised gold and white horse head with flowing mane forming the number 69"></div>

    <div class="invitation__frame"></div>
    <div class="corner-ornament corner-ornament--tl" role="img" aria-label="Gold floral corner ornament"></div>
    <div class="corner-ornament corner-ornament--tr" role="img" aria-label="Gold floral corner ornament"></div>
    <div class="corner-ornament corner-ornament--bl" role="img" aria-label="Gold floral corner ornament"></div>
    <div class="corner-ornament corner-ornament--br" role="img" aria-label="Gold floral corner ornament"></div>

    <h1 class="headline">
      <span class="headline__lead">You are invited to</span>
      <span class="headline__title">Year <small>of the</small> Horse</span>
    </h1>
    <h2 class="subtitle">Chinese New Year 2014 Celebration</h2>

    <div class="message">
      <p>We’d love you to join us as we celebrate<br>Chinese New Year 2014<br>with some great music, some<br>horse de’oveurs, exotic cocktails,<br>and top company.</p>
      <p>We’ll horse around a little as well :)</p>
    </div>

    <p class="hosts">~ Otto &amp; Lin ~</p>

    <div class="location-map" role="img" aria-label="Street map with a pin marking the party address"></div>

    <dl class="details">
      <div class="details__row"><dt>Party date:</dt> <dd>01 Feb 2014</dd></div>
      <div class="details__row"><dt>RSVP:</dt> <dd>22 Jan 2014 to lin@tealmeadow.net</dd></div>
      <div class="details__row details__indent">or otto@tealmeadow.net</div>
      <div class="details__row"><dt>Address:</dt> <dd>17 Marlow Crescent, Singapore 568213</dd></div>
    </dl>
  </main>
</body>
</html>
```